Business card design needed

I need a business card for my new Food & Lifestyle Coaching business - "Bloomwell Food & Lifestlye Coaching"

i already have a logo and would like to have that incorporated into the business card, obviously.

i would like a design that says "fresh" and "funky" - my target market is female, aged 20-45 so i want something that will stand out to them when they see it.

My "Company Colour" is Apple Green
Updates

Thankyou to everyone who has submitted a design for my project. At this stage i have quite a large number of designs to chose from and with only a short time until my project closes i am focusing now on chosing from those i have already shortlisted so am unfortunately not considering any new desings.

Thankyou again for your interest in my project.

Target Market(s)

Female, Health Conscious (or looking to improve their health/lifestyle), aged between 20-45

Industry/Entity Type

Business

Contact Information for Business Card

Tessa Harlow
Ph: 0438215790
Email: hellobloom@quarlmail.com

Requirements
Must have
• Must include my existing Logo
Nice to have
• Would be nice to incoirporate and appointment card on the back

```html
<!DOCTYPE html>
<html lang="en">
<head>
<meta charset="utf-8">
<title>Bloomwell – Business Card &amp; Appointment Card</title>
<link rel="stylesheet" href="https://fonts.googleapis.com/css2?family=Open+Sans:ital,wght@0,400;0,600;1,400;1,700&display=swap">
<style>
  :root {
    --apple-green: #9bbe12;
    --ink: #231f20;
    --paper: #ffffff;
    --label-grey: #4a4a4a;
    --backdrop: #e9e9e6;
  }
  * { box-sizing: border-box; margin: 0; padding: 0; }
  html, body { width: 1200px; height: 900px; overflow: hidden; }
  body {
    background: var(--backdrop);
    font-family: "Open Sans", Arial, sans-serif;
    position: relative;
  }

  .card {
    position: absolute;
    border-radius: 16px;
    overflow: hidden;
    box-shadow: 0 4px 14px rgba(0,0,0,0.18);
  }

  /* Front */
  .card-front {
    left: 186px; top: 307px;
    width: 515px; height: 285px;
    background: var(--paper);
  }
  .card-front .band {
    position: absolute; left: 0; top: 0;
    width: 515px; height: 285px;
  }
  .brand {
    position: absolute;
    display: flex; align-items: center; gap: 12px;
    color: var(--ink);
    font-weight: 600;
  }
  .brand-dot {
    width: 22px; height: 22px; border-radius: 50%;
    background: var(--apple-green); flex: none;
  }
  .brand-text { display: flex; flex-direction: column; line-height: 1; }
  .brand-name { letter-spacing: -0.5px; }
  .card-front .brand { left: 62px; top: 48px; }
  .card-front .brand-dot { width: 44px; height: 44px; }
  .card-front .brand-name { font-size: 58px; }
  .card-front .brand-tagline { font-size: 15px; margin-top: 10px; margin-left: 66px; }

  .person, .contact {
    position: absolute; color: var(--paper); font-style: italic;
  }
  .person { left: 34px; top: 210px; }
  .person-name { font-size: 21px; font-weight: 700; line-height: 1.15; }
  .person-role { font-size: 16px; line-height: 1.3; }
  .contact { left: 262px; top: 214px; font-size: 16px; line-height: 1.4; }
  .contact b { font-weight: 700; }

  /* Back */
  .card-back {
    left: 729px; top: 193px;
    width: 286px; height: 513px;
    background: var(--apple-green);
  }
  .card-back .brand { left: 34px; top: 52px; gap: 8px; }
  .card-back .brand-dot { width: 26px; height: 26px; background: var(--paper); }
  .card-back .brand-name { font-size: 38px; }
  .card-back .brand-tagline { font-size: 10px; margin-top: 6px; margin-left: 40px; }

  .appointment-title {
    position: absolute; left: 0; top: 162px; width: 100%;
    text-align: center; color: var(--paper);
    font-style: italic; font-size: 24px;
  }
  .fields { position: absolute; left: 29px; top: 212px; width: 228px; }
  .field {
    height: 57px; margin-bottom: 18px;
    background: var(--paper);
    border: 2px solid var(--ink);
    border-radius: 29px;
    text-align: center;
    padding-top: 6px;
    font-size: 12px; font-style: italic; color: var(--label-grey);
  }
</style>
</head>
<body>

<section class="card card-front" aria-label="Business card front">
  <svg class="band" viewBox="0 0 515 285" aria-hidden="true">
    <path d="M0 170 Q260 196 515 186 L515 192 Q260 200 0 176 Z" fill="var(--ink)"/>
    <path d="M0 174 Q260 198 515 190 L515 285 L0 285 Z" fill="var(--apple-green)"/>
  </svg>

  <div class="brand">
    <span class="brand-dot"></span>
    <span class="brand-text">
      <span class="brand-name">Bloomwell</span>
      <span class="brand-tagline">Food &amp; Lifestlye Coaching</span>
    </span>
  </div>

  <div class="person">
    <p class="person-name">Tessa Harlow</p>
    <p class="person-role">founder &amp; owner</p>
  </div>
  <div class="contact">
    <p><b>P:</b> 0438215790</p>
    <p><b>E:</b> hellobloom@quarlmail.com</p>
  </div>
</section>

<section class="card card-back" aria-label="Appointment card back">
  <div class="brand">
    <span class="brand-dot"></span>
    <span class="brand-text">
      <span class="brand-name">Bloomwell</span>
      <span class="brand-tagline">Food &amp; Lifestlye Coaching</span>
    </span>
  </div>

  <h2 class="appointment-title">Appointment</h2>

  <div class="fields">
    <div class="field">Name:</div>
    <div class="field">Date:</div>
    <div class="field">Time:</div>
    <div class="field">Location:</div>
  </div>
</section>

</body>
</html>
```